Etiketten für Gin
Zielgruppe
Wir sind eine kleine neue Brennerei im bayerischen Oberland und werden unter den Namen „Morgentau“ und „Morgentau Zitrone“ zwei GIN-Sorten auf den Markt bringen.
Der GIN wird online und vor Ort verkauft und sollte daher eine exklusiv-auffällige Optik haben um die Kunden zu beeindrucken. Zielkunden sind anspruchsvolle Genießer, welche die bayerische Gastlichkeit und Lebenskultur schätzen.
Neu an den beiden Gins ist, dass sie mit Blütenpollen destilliert werden, was auf dem Etikett erscheinen muss.
Aufgabenstellung
Wir suchen zwei sich ähnelnde GIN-Etiketten deren Design ausdrückt, dass es sich um handgemachte und hochwertige GIN handelt, deren Zutat Blütenpollen bisher einzigartig ist.
Statt der oft üblichen Bezeichnung „London Dry Gin“ soll „Hochbrand Dry Gin“ und „handcrafted“ auf dem Etikett erscheinen, zusätzlich natürlich die verkehrsüblichen Angaben.
Abgefüllt wird in weißen 500ml Flaschen Typ Ventra mit Korkverschluss von flaschenhof-beispiel.com.
Sinnvoll halten wir ein Frontetikett, lassen aber gerne auch andere Vorschläge zu.

```html
<!DOCTYPE html>
<html lang="de">
<head>
<meta charset="utf-8">
<title>Morgentau Zitrone – Etikett</title>
<link href="https://fonts.googleapis.com/css2?family=Arvo&family=Josefin+Sans:wght@300;400&family=Questrial&family=Poppins:wght@600;700&display=swap" rel="stylesheet">
<style>
  :root {
    --band-yellow: #f5d033;
    --title-yellow: #f6d53c;
    --lemon-light: #fde04a;
    --lemon-dark: #f3cf2c;
    --leaf-green: #8a9a40;
    --ink: #3e3e3e;
    --paper: #ffffff;
  }
  html, body {
    margin: 0;
    padding: 0;
    overflow: hidden;
    background: var(--paper);
  }
  .label {
    position: relative;
    width: 1200px;
    height: 800px;
    background: var(--paper);
    overflow: hidden;
    color: var(--ink);
  }
  .band {
    position: absolute;
    left: 0;
    width: 1200px;
    height: 60px;
    background: var(--band-yellow);
  }
  .band--top { top: 0; }
  .band--bottom { bottom: 0; }

  .lemon-art {
    position: absolute;
    left: 525px;
    top: 80px;
    width: 150px;
    height: 158px;
    border-radius: 40% 40% 46% 46%;
    background: linear-gradient(180deg, var(--leaf-green) 0%, var(--leaf-green) 22%, var(--lemon-light) 38%, var(--lemon-dark) 100%);
  }

  .product-name {
    position: absolute;
    left: 0;
    top: 238px;
    width: 1200px;
    margin: 0;
    text-align: center;
    font-family: "Arvo", serif;
    font-weight: 400;
    font-size: 92px;
    line-height: 150px;
    color: var(--title-yellow);
    letter-spacing: 1px;
  }
  .product-name span { display: block; }

  .gin-type {
    position: absolute;
    left: 0;
    top: 580px;
    width: 1200px;
    margin: 0;
    text-align: center;
    font-family: "Josefin Sans", sans-serif;
    font-weight: 400;
    font-size: 20px;
    line-height: 25px;
    letter-spacing: 2.5px;
    color: var(--ink);
    text-transform: uppercase;
  }
  .volume {
    position: absolute;
    left: 0;
    top: 706px;
    width: 1200px;
    margin: 0;
    text-align: center;
    font-family: "Poppins", sans-serif;
    font-weight: 700;
    font-size: 19px;
    letter-spacing: 2px;
    color: var(--ink);
  }

  .story {
    position: absolute;
    left: 33px;
    top: 234px;
    width: 215px;
    margin: 0;
    font-family: "Questrial", sans-serif;
    font-size: 13px;
    line-height: 23.5px;
    letter-spacing: 0.6px;
    color: var(--ink);
  }
  .story p { margin: 0; }
  .story p + p { margin-top: 24px; }

  .distributor {
    position: absolute;
    left: 920px;
    top: 287px;
    width: 200px;
    margin: 0;
    text-align: center;
    font-family: "Questrial", sans-serif;
    font-size: 9.5px;
    line-height: 12px;
    letter-spacing: 0.6px;
    text-transform: uppercase;
    color: var(--ink);
  }
  .recycle-note {
    position: absolute;
    left: 940px;
    top: 468px;
    width: 203px;
    margin: 0;
    text-align: right;
    font-family: "Poppins", sans-serif;
    font-weight: 600;
    font-size: 9.5px;
    line-height: 17px;
    letter-spacing: 0.4px;
    color: var(--ink);
  }
</style>
</head>
<body>
<main class="label">
  <div class="band band--top"></div>

  <section class="story">
    <p>Wir sind eine kleine neue Brauerei im bayerischer Oberland. Das neue an unserem Gin ist, dass sie mit Blütenpollen destilliert wird. Unser hochwertiger Gin wird in Handarbeit gefertigt. Zur destilierung nutzen wir Blütenpollen was bisher einzigartig ist.</p>
    <p>Hier könnten Inhaltsangaben und Alkoholgehalt stehen</p>
  </section>

  <div class="lemon-art" role="img" aria-label="Illustration: zwei Zitronen mit grünen Blättern"></div>

  <h1 class="product-name"><span>Morgentau</span><span>Zitrone</span></h1>

  <p class="gin-type">Hochbrand Dry Gin<br>–<br>Handcrafted</p>

  <p class="volume">500 ML</p>

  <p class="distributor">Vertrieben durch:<br>Name der Brennerei<br>mit Anschrift</p>

  <p class="recycle-note">Bitte recyceln Sie diese Flasche<br>nach der Verwendung.</p>

  <div class="band band--bottom"></div>
</main>
</body>
</html>
```